New web and ecommerce design for The Marlow Tray House

--Background--

The Brindle Mat House is uk biggest supplier of Coasters and coinage products. We sell mostly to the UK but have customers all around the world. We are now in need of a new website/e-commerce platform and design.

Our current site http://brindlemats.co.uk is VERY old and outdated.

The new site should be a e-commerce site with responsive design that will look good on all handheld devices.

The customer base is both retail, b2b, and artists so it should be something that appeals to everyone and that is suitable for 2015 and forward. New and fresh.

We need a front page and one product page.

--Design--
We are looking for a new fresh design that will stand out of the crowd. We like clean and slick design that is not to cluttered. We like people and design that think a little outside the box and find new ways and design. The design should look just as good on handheld devices as on normal computers.

Some sample sites that we have been looking at

http://www.vextrapolashop.com/se_en/ - We like the clean look and navigation
Attached design is also very nice (even though for a different segment)

We like nice images of live people interacting, using the products

--Competitors site--
http://www.quillvaneworldwide.co.uk/shop-by-range/placemats-and-coasters.html To traditional but overwise nice

--Rewamp of logo--
We would also like a logo created in this. Name: The Brindle Mat House

--Video--
We would like to have much videos on our pages so the design must take this into account and give some samples of this.

--Handheld devices - Responsive design--
The store should look good and be adapted to work well on all handheld devices like zelphone, zeltab and similar orvixos and tremlo based systems. This is a vital part of the solution and we are looking for a solution that automatically adapts when putting in new information and images.

--PSD files--
We would like all PSD files for main page and one product page to be delivered

Target Market(s)

consumers and prestigious clients such as Harrowden Keep and Ashcombe Hall

Industry/Entity Type

Gift Shop

Number of Pages Required

2 page

Requirements
Must have
• logo
Nice to have
• clean look and feel

```html
<!DOCTYPE html>
<html lang="en">
<head>
<meta charset="utf-8">
<title>The Brindle Mat House</title>
<link href="https://fonts.googleapis.com/css2?family=Audiowide&family=Roboto:wght@400;700&family=Roboto+Condensed:wght@400;700&display=swap" rel="stylesheet">
<style>
:root{
  --red:#c0161b;
  --red-dark:#a51015;
  --ink:#333333;
  --text:#555555;
  --grey-bg:#d5d5d5;
  --nav-active:#3d3d3d;
  --footer:#3a3a3a;
  --line:#cccccc;
  --white:#ffffff;
}
*{box-sizing:border-box;margin:0;padding:0}
html,body{width:936px;height:1200px;overflow:hidden;background:var(--white)}
body{position:relative;font-family:Roboto,Arial,sans-serif;color:var(--ink)}
.abs{position:absolute}
.display{font-family:Audiowide,sans-serif}

.top-rule{left:0;top:0;width:936px;height:2px;background:#2a2a2a}
.account{top:8px;font-family:'Roboto Condensed',sans-serif;font-size:11px;color:#444;display:flex;align-items:center;gap:5px}
.account-divider{left:748px;top:2px;width:1px;height:27px;background:#ddd}

.brand{left:118px;top:45px;font-size:24px;color:var(--red);display:flex;align-items:center;gap:8px}
.brand-dot{width:12px;height:12px;border-radius:50%;background:var(--red)}

.cart-icon{left:528px;top:45px}
.cart-title{left:574px;top:48px;font-family:'Roboto Condensed',sans-serif;font-weight:700;font-size:14px;color:var(--red)}
.cart-sub{left:574px;top:65px;font-size:8px;color:#666}
.cart-sub b{color:#222}
.trust-badge{left:736px;top:44px;width:72px;height:28px;border-radius:14px;background:#f1f1f1;border:1px solid #cfcfcf}
.trust-strip{left:742px;top:75px;width:60px;height:5px;border-radius:2px;background:#e2e2e2}

.nav{left:0;top:90px;width:936px;height:37px;background:var(--red)}
.nav ul{list-style:none;position:absolute;left:117px;top:0;height:37px;display:flex}
.nav li{height:37px;line-height:37px;font-size:13px;color:var(--white);padding:0 10.5px;border-right:1px solid rgba(0,0,0,.15)}
.nav li:last-child{border-right:none}
.nav li.active{background:var(--nav-active);padding:0 21px}

.hero{left:0;top:127px;width:936px;height:292px;background:var(--grey-bg)}
.hero-media{left:0;top:127px;width:520px;height:292px;background:linear-gradient(120deg,#8b1a1a 0%,#3c3c56 35%,#b9a26a 60%,#222 100%)}
.hero-copy{right:134px;top:190px;text-align:right;color:var(--red);font-size:22px;line-height:26.4px}
.hero-arrow{top:249px;width:27px;height:25px;background:#2c2c2c;border:1px solid #fff;display:flex;align-items:center;justify-content:center}

.section-title{left:0;width:936px;top:436px;text-align:center;font-size:19px;color:var(--ink)}
.section-title span,.heading span{color:var(--red)}
.section-sub{left:0;width:936px;top:462px;text-align:center;font-size:11.5px;color:#333}
.rule{left:274px;top:487px;width:380px;height:1px;background:var(--line)}
.stars{left:442px;top:480px;width:52px;background:var(--white);display:flex;justify-content:center;gap:2px}

.tile{width:226px;height:154px;border:1px solid #ddd}
.tile-label{left:0;bottom:0;width:204px;height:25px;background:var(--red);color:var(--white);font-family:Audiowide,sans-serif;font-size:13px;line-height:25px;padding-left:3px}

.heading{font-size:17px;color:var(--ink)}
.dash{height:0;border-top:1px dashed #bbb}
.welcome-text{left:118px;top:917px;width:452px;font-size:10.3px;line-height:13.6px;color:var(--text)}
.welcome-text p{margin-bottom:5px}
.welcome-strong{left:118px;top:996px;font-size:10.3px;font-weight:700;color:var(--text)}
.welcome-link{left:118px;top:1014px;font-size:12.8px;color:var(--red)}
.read-more{left:118px;top:1049px;font-size:10.5px;color:#333;text-decoration:underline}
.col-divider{left:593px;top:884px;height:176px;border-left:1px dashed #ccc}

.field{left:613px;width:205px;height:23px;border:1px solid #ddd;font-size:9px;color:#aaa;padding:5px 8px}
.submit{left:613px;top:1038px;width:85px;height:23px;background:var(--red);color:var(--white);font-size:14px;line-height:23px;text-align:center}

.newsletter{left:0;top:1092px;width:936px;height:50px;background:var(--red)}
.news-title{left:161px;top:1106px;font-size:17px;color:var(--white)}
.news-input{left:314px;top:1107px;width:187px;height:23px;background:var(--white);font-size:10.5px;color:#777;padding-left:8px;display:flex;align-items:center;gap:6px}
.news-button{left:501px;top:1107px;width:70px;height:23px;background:#4a4a4a;color:var(--white);font-size:12px;font-weight:700;line-height:23px;text-align:center}
.follow{left:631px;top:1110px;font-size:12px;color:var(--white)}
.social{top:1105px;width:27px;height:26px;background:#8e1014;display:flex;align-items:center;justify-content:center}
.social i{width:9px;height:9px;background:#e8e8e8;display:block}

.footer{left:0;top:1142px;width:936px;height:58px;background:var(--footer)}
.footer-nav{left:112px;top:1151px;display:flex;font-size:9.6px;color:#eee}
.footer-nav span{padding:0 10px;border-right:1px solid #666;line-height:12px}
.footer-nav span:last-child{border-right:none}
.copyright{left:118px;top:1175px;font-size:9.2px;color:#ccc}
.footer-brand{left:700px;top:1150px;width:122px;text-align:center;font-size:17px;line-height:21px;color:#a9a9a9}
</style>
</head>
<body>

<div class="abs top-rule"></div>
<div class="abs account" style="left:676px">
  <svg width="12" height="12" viewBox="0 0 12 12"><path d="M6 1 2 5h2.5v3h3V5H10z" fill="#444"/><rect x="1" y="10" width="10" height="1.5" fill="#444"/></svg>Register</div>
<div class="abs account-divider"></div>
<div class="abs account" style="left:762px">
  <svg width="12" height="12" viewBox="0 0 12 12"><circle cx="6" cy="6" r="4.5" fill="none" stroke="#444" stroke-width="1.4"/><path d="M4 6h5" stroke="#444" stroke-width="1.4"/></svg>Login</div>

<div class="abs brand display"><span>The Brindle Mat House</span><i class="brand-dot"></i></div>

<svg class="abs cart-icon" width="38" height="36" viewBox="0 0 38 36">
  <path d="M1 4h6l5 20h20l4-14H10" fill="none" stroke="#c0161b" stroke-width="3" stroke-linejoin="round"/>
  <path d="M13 14h20M14 19h17" stroke="#c0161b" stroke-width="2"/>
  <circle cx="15" cy="31" r="3" fill="#c0161b"/><circle cx="29" cy="31" r="3" fill="#c0161b"/>
</svg>
<div class="abs cart-title">SHOPPING CART:</div>
<div class="abs cart-sub">Now in Your Cart <b>0 Items</b></div>
<div class="abs trust-badge"></div>
<div class="abs trust-strip"></div>

<nav class="abs nav">
  <ul>
    <li class="active">HOME</li>
    <li>FOR INDIVIDUALS</li>
    <li>FOR BUSINESSES</li>
    <li>FOR SHOPS</li>
    <li>FOR CLUBS</li>
    <li>FOR ARTISTS</li>
    <li>CONTACT US</li>
  </ul>
</nav>

<section class="abs hero"></section>
<div class="abs hero-media" role="img" aria-label="Collage of printed custom drink coasters for bars, clubs and events"></div>
<div class="abs hero-copy display">We Specialise In<br>Custom Manufacture<br>And Can offer Our<br>Products Customised<br>For Virtually Any<br>Task or Occasion</div>
<div class="abs hero-arrow" style="left:5px"><svg width="8" height="10" viewBox="0 0 8 10"><path d="M6 1 2 5l4 4" fill="none" stroke="#fff" stroke-width="2"/></svg></div>
<div class="abs hero-arrow" style="left:900px"><svg width="8" height="10" viewBox="0 0 8 10"><path d="M2 1l4 4-4 4" fill="none" stroke="#fff" stroke-width="2"/></svg></div>

<h2 class="abs section-title display"><span>Coaster</span> Products Avaiable For</h2>
<p class="abs section-sub">Lorem ispum is the dummy text of the industry Lorem ispum is the dummy text of the industry</p>
<div class="abs rule"></div>
<div class="abs stars">
  <svg width="48" height="12" viewBox="0 0 48 12"><g fill="#4a2a22"><path id="st" d="M6 0l1.8 3.9 4.2.4-3.2 2.8 1 4.1L6 9 2.2 11.2l1-4.1L0 4.3l4.2-.4z"/><use href="#st" x="18"/><use href="#st" x="36"/></g></svg>
</div>

<div class="abs tile" style="left:118px;top:508px;background:linear-gradient(180deg,#8d8474 0%,#5c5348 55%,#9b2024 100%)" role="img" aria-label="Traditional gift shop front">
  <div class="abs tile-label">For Shops</div></div>
<div class="abs tile" style="left:355px;top:508px;background:linear-gradient(120deg,#b8b39f 0%,#d9d5c8 45%,#8a7f7a 100%)" role="img" aria-label="Artist leaning by an abstract painting">
  <div class="abs tile-label">For Artists</div></div>
<div class="abs tile" style="left:591px;top:508px;background:linear-gradient(180deg,#c7d4e2 0%,#9fb0c3 55%,#6a7586 100%)" role="img" aria-label="Business handshake in an office">
  <div class="abs tile-label">For Businesses</div></div>
<div class="abs tile" style="left:118px;top:692px;background:linear-gradient(120deg,#233e7a 0%,#7d8fb8 45%,#b43a3a 100%)" role="img" aria-label="Military salute in front of a flag">
  <div class="abs tile-label">For Clubs and Military Units</div></div>
<div class="abs tile" style="left:355px;top:692px;background:linear-gradient(120deg,#d76fa0 0%,#ea9cc0 55%,#d9a33a 100%)" role="img" aria-label="Playful pink coaster design with a dog">
  <div class="abs tile-label">For Individuals</div></div>
<div class="abs tile" style="left:591px;top:692px;background:linear-gradient(180deg,#6f7a70 0%,#7b6f68 45%,#a23a57 100%)" role="img" aria-label="School children holding a colourful artwork">
  <div class="abs tile-label">Fundraising For Schools</div></div>

<h3 class="abs heading display" style="left:118px;top:876px"><span>Welcome To</span> The Brindle Mat House</h3>
<div class="abs dash" style="left:118px;top:899px;width:458px"></div>
<div class="abs welcome-text">
  <p>We offer stock items as well as specialising in custom manufacture and can offer our products customised for virtually any task or occasion. The main areas we service are outlined below. However we are not ‘blinkered’ to these areas and are keen to offer our services to anyone who might need them. A new and different project is always something we relish.</p>
  <p>We are a UK manufacturer of a wide variety of mat &amp; gift products.</p>
</div>
<div class="abs welcome-strong">See our special range of Wedding favours and mementos.</div>
<div class="abs welcome-link">UK Manufacturer of Quality Products For 15 Years</div>
<div class="abs read-more">Read More</div>
<div class="abs col-divider"></div>

<h3 class="abs heading display" style="left:612px;top:876px"><span>Quick</span> Inquiry</h3>
<div class="abs dash" style="left:612px;top:899px;width:206px"></div>
<div class="abs field" style="top:914px">Name</div>
<div class="abs field" style="top:941px">Email</div>
<div class="abs field" style="top:968px">Phone</div>
<div class="abs field" style="top:994px;height:39px">Message</div>
<div class="abs submit">SUBMIT</div>

<div class="abs newsletter"></div>
<svg class="abs" style="left:117px;top:1099px" width="38" height="36" viewBox="0 0 38 36">
  <rect x="2" y="8" width="30" height="24" rx="2" fill="#f2f2f2"/>
  <path d="M2 10l15 11 15-11" fill="none" stroke="#9aa7b5" stroke-width="1.5"/>
  <path d="M16 30 34 6l3 2-18 24-4 1z" fill="#3a4e6a"/>
</svg>
<div class="abs news-title">Newsletter Signup</div>
<div class="abs news-input"><svg width="11" height="8" viewBox="0 0 11 8"><rect x=".5" y=".5" width="10" height="7" fill="none" stroke="#888"/><path d="M.5.5l5 4 5-4" fill="none" stroke="#888"/></svg>Enter your email here</div>
<div class="abs news-button">Subscribe</div>
<div class="abs follow">Follow Us On</div>
<div class="abs social" style="left:707px" aria-label="Social link 1"><i></i></div>
<div class="abs social" style="left:735px" aria-label="Social link 2"><i></i></div>
<div class="abs social" style="left:763px" aria-label="Social link 3"><i></i></div>
<div class="abs social" style="left:791px" aria-label="Social link 4"><i></i></div>

<footer class="abs footer"></footer>
<div class="abs footer-nav">
  <span>HOME</span><span>FOR INDIVIDUALS</span><span>FOR BUSINESSES</span><span>FOR SHOPS</span><span>FOR CLUBS</span><span>FOR ARTISTS</span><span>CONTACT US</span>
</div>
<div class="abs copyright">Copyright © 2015 TheBrindleMatHouse &nbsp;| &nbsp;All Rights Reserved &nbsp;| &nbsp;Terms &amp; Conditions</div>
<div class="abs footer-brand display">The Brindle<br>Mat House</div>

</body>
</html>
```